Presence Leadership Model

I am looking for a graphic design of the attached leadership model. The colors and design can be altered in any manner that brings the model alive version of the house model.

```html
<!DOCTYPE html>
<html lang="en">
<head>
<meta charset="utf-8">
<title>Presence Leadership Model</title>
<link rel="stylesheet" href="https://fonts.googleapis.com/css2?family=Nunito+Sans:wght@400;600;700&display=swap">
<style>
  :root {
    --ink: #4a4466;
    --white: #ffffff;
    --roof-left: #2f3769;
    --roof-mid: #6a5069;
    --roof-right: #a87b7c;
    --org-top: #463d72;
    --org-bottom: #8d83a9;
    --inter-top: #6c5b88;
    --inter-bottom: #a695b3;
    --personal-top: #a67682;
    --personal-bottom: #b89eb3;
    --inner-top: #8a8fb2;
    --inner-bottom: #7a9aa9;
    --arrow-left: #5a4c7e;
    --arrow-right: #9b7486;
  }
  * { margin: 0; padding: 0; box-sizing: border-box; }
  html, body { width: 1200px; height: 1200px; overflow: hidden; background: var(--white); }
  body { font-family: "Nunito Sans", "Avenir Next", sans-serif; color: var(--white); }
  .model { position: relative; width: 1200px; height: 1200px; }

  .roof { position: absolute; left: 0; top: 0; }
  .roof-title {
    position: absolute; left: 0; width: 1200px; top: 164px;
    text-align: center; font-size: 34px; font-weight: 700; line-height: 40px;
  }
  .roof-tagline {
    position: absolute; left: 0; width: 1200px; top: 228px;
    text-align: center; font-size: 22px; font-weight: 400; line-height: 35px;
  }

  .band-heading {
    position: absolute; left: 0; width: 1200px; text-align: center;
    color: var(--ink); font-size: 24px; font-weight: 600; line-height: 30px;
  }
  .band-heading.outer { top: 361px; }
  .band-heading.inner { top: 843px; }

  .pillar {
    position: absolute; top: 404px; height: 426px;
    text-align: center; padding-top: 28px;
  }
  .pillar.organisation { left: 45px; width: 323px; background: linear-gradient(170deg, var(--org-top), var(--org-bottom)); }
  .pillar.interpersonal { left: 423px; width: 353px; background: linear-gradient(170deg, var(--inter-top), var(--inter-bottom)); }
  .pillar.personal { left: 832px; width: 345px; background: linear-gradient(170deg, var(--personal-top), var(--personal-bottom)); }

  .pillar-title { font-size: 28px; font-weight: 700; line-height: 34px; }
  .pillar-method {
    margin-top: 6px; font-size: 22px; font-weight: 700; line-height: 28px;
    text-decoration: underline; text-underline-offset: 4px; text-decoration-thickness: 1.5px;
  }
  .practice-list { list-style: none; font-size: 18.5px; line-height: 27px; font-weight: 400; }
  .practice-list li { position: relative; }
  .practice-list li::before {
    content: ""; position: absolute; top: 9px;
    width: 9px; height: 9px; border-radius: 50%; background: var(--white);
  }

  .organisation .practice-list { margin-top: 43px; padding: 0 24px 0 40px; }
  .organisation .practice-list li::before { left: -19px; }
  .interpersonal .practice-list { margin-top: 31px; padding: 0 40px 0 60px; }
  .interpersonal .practice-list li::before { left: -21px; }
  .personal .practice-list { margin-top: 71px; text-align: left; padding-left: 83px; }
  .personal .practice-list li::before { left: -18px; }

  .flow-arrow { position: absolute; top: 603px; }
  .flow-arrow.to-organisation { left: 376px; }
  .flow-arrow.to-interpersonal { left: 782px; }

  .foundation {
    position: absolute; top: 887px; height: 212px;
    background: linear-gradient(175deg, var(--inner-top), var(--inner-bottom));
    display: flex; flex-direction: column; align-items: center;
    padding-top: 48px; gap: 44px;
  }
  .foundation.organisation { left: 47px; width: 321px; }
  .foundation.interpersonal { left: 423px; width: 353px; }
  .foundation.personal { left: 832px; width: 345px; }
  .wellbeing-item {
    font-size: 22px; font-weight: 700; line-height: 28px;
    text-decoration: underline; text-underline-offset: 4px; text-decoration-thickness: 1.5px;
  }
</style>
</head>
<body>
<main class="model">
  <svg class="roof" width="1200" height="360" viewBox="0 0 1200 360" aria-hidden="true">
    <defs>
      <linearGradient id="roofFill" x1="0" y1="0" x2="1" y2="0.3">
        <stop offset="0" stop-color="var(--roof-left)"/>
        <stop offset="0.5" stop-color="var(--roof-mid)"/>
        <stop offset="1" stop-color="var(--roof-right)"/>
      </linearGradient>
    </defs>
    <polygon points="611,103 49,348 1172,348" fill="url(#roofFill)"/>
  </svg>
  <h1 class="roof-title">Presence</h1>
  <p class="roof-tagline">Foster contagious success through people,<br>relationships and a shared vision</p>

  <h2 class="band-heading outer">Outer (Impact) Strategies</h2>

  <section class="pillar organisation">
    <h3 class="pillar-title">Organisation Level</h3>
    <p class="pillar-method">Wins Theory</p>
    <ul class="practice-list">
      <li>Develop concrete outcomes,<br>and visible results</li>
      <li>Foster in-depth changes,<br>and new practices</li>
      <li>Have a micro, interpersonal<br>or local impact</li>
      <li>Cultivate positive judgment,<br>and shared ambition</li>
    </ul>
  </section>

  <section class="pillar interpersonal">
    <h3 class="pillar-title">Interpersonal Level</h3>
    <p class="pillar-method">Heart Listening</p>
    <ul class="practice-list">
      <li>Ask open-ended questions</li>
      <li>Affirm someone’s strengths,<br>efforts and past success</li>
      <li>Reflect back what is shared<br>for confirmation</li>
      <li>Summarise key points to<br>gain insights</li>
      <li>Share and develop mutual<br>expertise</li>
    </ul>
  </section>

  <section class="pillar personal">
    <h3 class="pillar-title">Personal Level</h3>
    <p class="pillar-method">Clear Dialogue</p>
    <ul class="practice-list">
      <li>Stop</li>
      <li>Settle</li>
      <li>Welcome</li>
      <li>Notice What Arises</li>
      <li>Hear Fully</li>
      <li>Say What Is Real</li>
    </ul>
  </section>

  <svg class="flow-arrow to-organisation" width="44" height="32" viewBox="0 0 44 32" aria-hidden="true">
    <polygon points="0,16 18,1 18,9 42,9 42,23 18,23 18,31" fill="var(--arrow-left)"/>
  </svg>
  <svg class="flow-arrow to-interpersonal" width="44" height="32" viewBox="0 0 44 32" aria-hidden="true">
    <polygon points="0,16 18,1 18,9 42,9 42,23 18,23 18,31" fill="var(--arrow-right)"/>
  </svg>

  <h2 class="band-heading inner">Inner (Wellbeing) Strategies</h2>

  <section class="foundation organisation">
    <p class="wellbeing-item">Physical Fitness</p>
    <p class="wellbeing-item">Nutrition</p>
  </section>
  <section class="foundation interpersonal">
    <p class="wellbeing-item">Heart Rate Variability</p>
    <p class="wellbeing-item">Neurofeedback</p>
  </section>
  <section class="foundation personal">
    <p class="wellbeing-item">Island Hopping Club</p>
    <p class="wellbeing-item">Video Gaming Club</p>
  </section>
</main>
</body>
</html>
```